Online-Marketing Material für Beraternetzwerk
Zielgruppe
Ich habe ein Beraternetzwerk im deutschen Gesundheitswesen gegründet, gleichzeitig einen gemeinnützigen Verein, habe zwei webseiten www.kv-pflegeberatung-demo.de + www.kv-pflegefreunde-demo.de, Logo, Briefpapier etc. sind vorhanden. Hauptfarbe GmbH RGB 185/87/120 Hex#B95778, Verein RGB 226/125/119 Hex#E27D77. Die Organisationen sind grundsätzlich getrennt, aber es gibt eine Zusammenarbeit und Partner meines Netzwerkes sind auch Fördermitglieder im Verein
Aufgabenstellung
Die beiden Firmenfarben müssen verwendet werden, für die GmbH hauptsächlich die eigene, die 2. Farbe darf mit verwendet werden. Es darf insgesamt feminin wirken, aber nicht verspielt oder gar niedlich. Ich bin Business-Frau;-). Als Schrift habe ich mich auf Avenir next konzentriert, die Agentur hat auch Alternate Gothic auf den Webseiten verwendet. Jetzt benötige ich für eine Veranstaltungsreihe die Ausarbeitung von LinkedIn, Facebook/Insta, Einladung per Brevo und E-Mail Grafiken. Es sind immer Veranstaltungen, zu denen ich einlade und in denen meine Geschäftspartner ihre Expertise gegenüber Kunden darstellen. Die Veranstaltungen sind als Duo zu sehen 1. Präsenz in München, 2. als Online Meeting ein paar Tage später. Die Location wird das Hotel Marwin, direkt am Brunnenhofplatz in München sein. Start der Präsenzveranstaltung 11:00, anschließend Mittagessen. Als Titel für die Veranstaltungen sehe ich 'KlinikForum' vor, es wird jeweils noch ein inhaltliches Thema wie z.B. 'Unternehmenskauf/-verkauf' ergänzt. Erster Termin ist vss. am 15. September 2023. Anbei auch ein paar erste Entwürfe 'meiner' Agentur nebst Feedback von mir. Ich glaube inzwischen nicht, dass hier etwas vernünftiges produziert wird, deshalb mein Versuch auf diesem Weg. Weitere Zusammenarbeit dann herzlich gerne

```html
<!DOCTYPE html>
<html lang="de">
<head>
<meta charset="utf-8">
<title>KlinikForum – 15. September 2023</title>
<link rel="stylesheet" href="https://fonts.googleapis.com/css2?family=Mulish:wght@300;400;700;800;900&display=swap">
<style>
  :root {
    --brand: #c4577f;
    --brand-deep: #b95778;
    --blush-top: #e08aa8;
    --blush-mid: #f1c3d3;
    --white: #ffffff;
    --ink: #141414;
    --wall-light: #efe8de;
    --wall-mid: #e0d6c8;
    --wall-dark: #cdc1b0;
    --blazer: #5a5c62;
  }
  * { box-sizing: border-box; margin: 0; padding: 0; }
  html, body { width: 1200px; height: 630px; overflow: hidden; background: var(--white); }
  .banner {
    position: relative;
    width: 1200px;
    height: 630px;
    overflow: hidden;
    font-family: "Mulish", "Avenir Next", sans-serif;
    background: linear-gradient(180deg, var(--blush-top) 0%, var(--blush-mid) 30%, var(--white) 66%, var(--white) 100%);
  }
  .portrait {
    position: absolute;
    top: 0;
    left: 560px;
    width: 640px;
    height: 630px;
    background:
      radial-gradient(ellipse 170px 330px at 410px 470px, rgba(90,92,98,0.55) 0%, rgba(90,92,98,0) 100%),
      linear-gradient(165deg, var(--wall-light) 0%, var(--wall-mid) 55%, var(--wall-dark) 100%);
    -webkit-mask-image: linear-gradient(90deg, transparent 0%, rgba(0,0,0,0.6) 25%, #000 45%);
    mask-image: linear-gradient(90deg, transparent 0%, rgba(0,0,0,0.6) 25%, #000 45%);
  }
  .event-title {
    position: absolute;
    left: 36px;
    top: 40px;
    font-size: 112px;
    line-height: 1;
    color: var(--brand);
    letter-spacing: 1px;
    white-space: nowrap;
  }
  .event-title .light { font-weight: 300; }
  .event-title .bold { font-weight: 900; }
  .event-topic {
    position: absolute;
    left: 42px;
    top: 166px;
    font-size: 26px;
    font-weight: 700;
    color: var(--brand);
    letter-spacing: 0.5px;
  }
  .date-badge {
    position: absolute;
    left: 42px;
    top: 222px;
    width: 234px;
    height: 346px;
  }
  .date-badge svg { position: absolute; inset: 0; }
  .date-text {
    position: absolute;
    inset: 0;
    color: var(--white);
    text-align: center;
  }
  .date-day { position: absolute; left: 20px; top: 56px; font-size: 122px; font-weight: 800; line-height: 1; letter-spacing: -2px; }
  .date-month { position: absolute; left: 0; right: 0; top: 176px; font-size: 33px; font-weight: 400; line-height: 1; }
  .date-year { position: absolute; left: 0; right: 0; top: 210px; font-size: 76px; font-weight: 800; line-height: 1; }
  .event-details {
    position: absolute;
    left: 298px;
    top: 233px;
    width: 440px;
    text-align: center;
    color: var(--brand);
  }
  .venue { font-size: 35px; font-weight: 800; line-height: 1.1; }
  .venue-note { font-size: 19px; font-weight: 300; margin-top: 0; }
  .format { font-size: 36px; font-weight: 800; margin-top: 14px; line-height: 1.1; }
  .start-time { font-size: 74px; font-weight: 800; line-height: 1; margin-top: 0; letter-spacing: 2px; }
  .organizer {
    position: absolute;
    left: 308px;
    top: 458px;
    display: flex;
    align-items: center;
    gap: 24px;
  }
  .organizer-dot {
    width: 88px;
    height: 88px;
    border-radius: 50%;
    background: var(--brand);
  }
  .organizer-name {
    font-size: 32px;
    font-weight: 800;
    line-height: 1.12;
    color: var(--ink);
  }
</style>
</head>
<body>
  <main class="banner">
    <div class="portrait" role="img" aria-label="Porträtfoto der Gastgeberin im grauen Blazer mit verschränkten Armen vor einer hellen Steinwand"></div>

    <h1 class="event-title"><span class="light">KLINIK</span> <span class="bold">FORUM</span></h1>
    <p class="event-topic">Unternehmenskauf/-verkauf</p>

    <div class="date-badge">
      <svg width="234" height="346" viewBox="0 0 234 346" aria-hidden="true">
        <polygon points="0,0 234,46 234,346 0,290" fill="var(--brand)"/>
      </svg>
      <div class="date-text">
        <div class="date-day">15.</div>
        <div class="date-month">September</div>
        <div class="date-year">2023</div>
      </div>
    </div>

    <section class="event-details">
      <p class="venue">im Hotel Marwin</p>
      <p class="venue-note">direkt am Brunnenhofplatz</p>
      <p class="format">Präsenzveranstaltung</p>
      <p class="start-time">11:00</p>
    </section>

    <div class="organizer">
      <span class="organizer-dot" aria-hidden="true"></span>
      <span class="organizer-name">KV Pflegeberatung<br>GmbH</span>
    </div>
  </main>
</body>
</html>
```